Mara Joss Advisory Business Cards

Hi - using the information and logo provided I require a two sided business card designed with the following information. The business card is a 'mini card' 3.5" x 1.25".

Front of card should be the logo attached but inverted (so the background is the peach colour and the logo white).

Back should have these details. If we can't fit the Instragram and Facebook part can we just put the little logos.

Ruth Penderby

Art and Design Consultant
Dealer - Curator - Events - Styling - Creative Sourcing

P: 0462 913 058
E: ruth@marajossadvisory.example
W: www.marajossadvisory.example
I (instagram image please): marajossadvisory F (Facebook image please): MaraJossAdvisor

Target Market(s)

Galleries, artists, art buyers, interior design clients, event managers, creative types

Industry/Entity Type

Business

```html
<!DOCTYPE html>
<html lang="en">
<head>
<meta charset="utf-8">
<title>Mara Joss Advisory – Mini Business Cards</title>
<link rel="stylesheet" href="https://fonts.googleapis.com/css2?family=Mulish:wght@400;700&family=Tinos:ital,wght@1,700&display=swap">
<style>
  :root {
    --page: #ecebe8;
    --peach-deep: #f0b9a0;
    --peach-light: #f8dacd;
    --peach-mark: #eeb49a;
    --white: #ffffff;
    --crimson: #d4245a;
    --plum: #a8345a;
    --rose-band: #dc5a72;
    --shadow: rgba(0, 0, 0, 0.18);
  }
  * { margin: 0; padding: 0; box-sizing: border-box; }
  html, body {
    width: 1200px; height: 1000px; overflow: hidden;
    background: var(--page);
    font-family: "Mulish", "Century Gothic", sans-serif;
  }
  .sheet { position: relative; width: 1200px; height: 1000px; }
  .card {
    position: absolute; left: 150px;
    width: 900px; height: 322px;
    overflow: hidden;
    box-shadow: 0 4px 14px var(--shadow);
  }
  .card--front { top: 120px; background: var(--peach-deep); }
  .card--back { top: 550px; background: var(--white); }
  .card-shapes { position: absolute; inset: 0; width: 900px; height: 322px; }

  /* Front */
  .front-brand {
    position: absolute; left: 60px; top: 0; height: 322px; width: 230px;
    display: flex; align-items: center; gap: 12px;
    color: var(--white); font-weight: 700; font-size: 22px; line-height: 1.2;
  }
  .front-brand .dot { width: 18px; height: 18px; border-radius: 50%; background: var(--white); flex: none; }
  .front-mark {
    position: absolute; left: 470px; top: 0; width: 410px; height: 322px;
    display: flex; align-items: center;
    color: var(--peach-mark); font-weight: 700; font-size: 58px; line-height: 1.05;
  }

  /* Back */
  .holder { position: absolute; left: 34px; top: 48px; }
  .holder-name { color: var(--crimson); font-weight: 700; font-size: 24px; }
  .holder-title { color: var(--plum); font-size: 19px; margin-top: 4px; }
  .contacts { position: absolute; left: 36px; top: 160px; list-style: none; }
  .contacts li {
    display: flex; align-items: center; gap: 8px;
    color: var(--plum); font-size: 20px; height: 29px;
  }
  .contacts .icon { width: 20px; height: 20px; flex: none; }
  .contacts .square { width: 16px; height: 16px; margin: 0 2px; background: var(--plum); flex: none; }
  .back-mark {
    position: absolute; left: 470px; top: 0; width: 330px; height: 322px;
    display: flex; align-items: center;
    color: var(--white); font-weight: 700; font-size: 52px; line-height: 1.05;
  }
  .services {
    position: absolute; left: 810px; top: 0; width: 90px; height: 322px;
    display: flex; align-items: center; justify-content: center;
  }
  .services-text {
    transform: rotate(-90deg); white-space: nowrap;
    font-family: "Tinos", "Times New Roman", serif; font-style: italic; font-weight: 700;
    color: var(--white); font-size: 19px; line-height: 1.35; text-align: center;
  }
</style>
</head>
<body>
<main class="sheet">

  <section class="card card--front" aria-label="Card front">
    <svg class="card-shapes" viewBox="0 0 900 322" aria-hidden="true">
      <path d="M470 0 Q395 80 345 161 Q400 248 455 322 L900 322 L900 0 Z" fill="var(--peach-light)"/>
    </svg>
    <div class="front-brand"><span class="dot"></span><span>Mara Joss Advisory</span></div>
    <div class="front-mark">Mara Joss Advisory</div>
  </section>

  <section class="card card--back" aria-label="Card back">
    <svg class="card-shapes" viewBox="0 0 900 322" aria-hidden="true">
      <path d="M470 0 Q400 80 352 161 Q405 248 470 322 L810 322 L810 0 Z" fill="var(--peach-light)"/>
      <rect x="810" y="0" width="90" height="322" fill="var(--rose-band)"/>
    </svg>

    <div class="holder">
      <h1 class="holder-name">Ruth Penderby</h1>
      <p class="holder-title">Art and Design Consultant</p>
    </div>

    <ul class="contacts">
      <li>
        <svg class="icon" viewBox="0 0 20 20" aria-hidden="true"><path d="M2 8 Q10 2 18 8 L16 11 L13 9 L13 7 Q10 6 7 7 L7 9 L4 11 Z M5 12 H15 L16 17 H4 Z" fill="var(--plum)"/></svg>
        0462 913 058
      </li>
      <li>
        <svg class="icon" viewBox="0 0 20 20" aria-hidden="true"><rect x="2" y="5" width="16" height="11" fill="var(--plum)"/><path d="M2 5 L10 11 L18 5" stroke="var(--white)" stroke-width="1.5" fill="none"/></svg>
        ruth@marajossadvisory.example
      </li>
      <li>
        <svg class="icon" viewBox="0 0 20 20" aria-hidden="true"><g fill="none" stroke="var(--plum)" stroke-width="1.5"><circle cx="10" cy="10" r="7.5"/><ellipse cx="10" cy="10" rx="3.5" ry="7.5"/><path d="M2.5 10 H17.5"/></g></svg>
        www.marajossadvisory.example
      </li>
      <li><span class="square"></span>marajossadvisory</li>
      <li><span class="square"></span>MaraJossAdvisor</li>
    </ul>

    <div class="back-mark">Mara Joss Advisory</div>

    <div class="services">
      <p class="services-text">Dealer - Curator - Events<br>Styling - Creative Sourcing</p>
    </div>
  </section>

</main>
</body>
</html>
```